Korvesh Menu

Hi there,
My restaurant called "Korvesh" means Spice in hebrew.
We are middle eastern restaurant that specialist in dips,salads and hot bread baked on the spot and charcoal grilled meat skewers
The restaurant is pretty casual and the atmosphere is nice and customers feels like home.
on www.korvesh.com.au you can see photos of the restaurant and the food.
ill add up the menus that i would like to be design please and the logo that is on the front of the shop is been add up
thank you

Target Market(s)

The regulars of the restaurant is jewish/israelis

Industry/Entity Type

Restaurant

```html
<!DOCTYPE html>
<html lang="en">
<head>
<meta charset="utf-8">
<title>Korvesh – Entrée Menu</title>
<link href="https://fonts.googleapis.com/css2?family=Federo&family=Rosarivo:ital@0;1&display=swap" rel="stylesheet">
<style>
  :root {
    --parchment-light: #f1e3cb;
    --parchment-mid: #e6d2b2;
    --parchment-dark: #c9ad8a;
    --band-black: #1a1a1a;
    --logo-black: #111111;
    --title-red: #b3212f;
    --heading-blue: #2f3f8f;
    --price-blue: #3a4a96;
    --ink: #1c1a17;
    --rule: #d9a79b;
    --sun-yellow: #fbbd14;
    --sun-rule: #f6d77a;
    --grill-dark: #4a3c33;
    --grill-mid: #8a7463;
    --ember: #e0702e;
  }
  * { margin: 0; padding: 0; box-sizing: border-box; }
  html, body { width: 848px; height: 1200px; overflow: hidden; }
  body {
    position: relative;
    font-family: "Rosarivo", Georgia, serif;
    color: var(--ink);
    background: radial-gradient(ellipse at 50% 35%, var(--parchment-light) 0%, var(--parchment-mid) 55%, var(--parchment-dark) 100%);
  }
  .grill-photo {
    position: absolute; left: 0; top: 640px; width: 848px; height: 560px;
    background:
      radial-gradient(ellipse at 50% 100%, rgba(224,112,46,0.55) 0%, rgba(224,112,46,0) 45%),
      linear-gradient(180deg, rgba(138,116,99,0) 0%, rgba(138,116,99,0.75) 18%, var(--grill-mid) 40%, var(--grill-dark) 100%);
  }
  .top-band {
    position: absolute; left: 0; top: 51px; width: 848px; height: 157px;
    background: var(--band-black);
  }
  .brand {
    position: absolute; left: 308px; top: 0; width: 206px; height: 157px;
    background: var(--logo-black);
    display: flex; flex-direction: column; align-items: center; justify-content: center; gap: 14px;
  }
  .brand-name {
    font-family: "Rosarivo", Georgia, serif;
    color: #ffffff; font-size: 46px; line-height: 1;
  }
  .brand-dot { width: 14px; height: 14px; border-radius: 50%; background: #ffffff; }
  .page-title {
    position: absolute; top: 212px; width: 100%; text-align: center;
    font-family: "Federo", serif; font-size: 52px; color: var(--title-red); font-weight: 400;
  }
  .section-heading {
    position: absolute; width: 100%; text-align: center;
    color: var(--heading-blue); font-size: 23px; font-weight: 700;
  }
  .section-note {
    position: absolute; width: 100%; text-align: center;
    font-style: italic; font-size: 11px; font-weight: 700;
  }
  .menu-list { position: absolute; list-style: none; }
  .menu-item {
    display: flex; justify-content: space-between; align-items: baseline;
    height: 25.6px; padding-top: 3px;
    border-bottom: 1px solid var(--rule);
    font-size: 14px; font-weight: 700;
  }
  .price { color: var(--price-blue); font-size: 14px; }
  .starters-list { left: 267px; top: 348px; width: 314px; }
  .hummus-list { left: 209px; top: 570px; width: 431px; }
  .platter {
    position: absolute; left: 208px; top: 715px; width: 432px; height: 432px;
    border-radius: 50%; background: var(--sun-yellow);
  }
  .platter-heading {
    position: absolute; top: 134px; width: 100%; text-align: center;
    color: var(--title-red); font-size: 23px; font-weight: 700;
  }
  .platter-note {
    position: absolute; top: 162px; width: 100%; text-align: center;
    color: var(--heading-blue); font-style: italic; font-weight: 700; font-size: 11.5px;
  }
  .platter-list { position: absolute; top: 180px; list-style: none; width: 184px; }
  .platter-list.left { left: 24px; }
  .platter-list.right { left: 224px; }
  .platter-list li {
    height: 25.6px; padding-top: 5px; text-align: center;
    color: #ffffff; font-size: 13.5px;
    border-bottom: 1px solid var(--sun-rule);
  }
  .platter-list li:last-child { border-bottom: none; }
</style>
</head>
<body>
  <div class="grill-photo" role="img" aria-label="Meat skewers over a glowing charcoal grill"></div>

  <header class="top-band">
    <div class="brand">
      <span class="brand-name">Korvesh</span>
      <span class="brand-dot"></span>
    </div>
  </header>

  <h1 class="page-title">Entrée</h1>

  <h2 class="section-heading" style="top:318px;">Starters</h2>
  <ul class="menu-list starters-list">
    <li class="menu-item"><span>6 Falafel Balls On Tahini</span><span class="price">$5.00</span></li>
    <li class="menu-item"><span>Moroccan Beef Cigars (3 per serve)</span><span class="price">$10.00</span></li>
    <li class="menu-item"><span>Fried Cauliflower</span><span class="price">$8.00</span></li>
    <li class="menu-item"><span>Pan Fried Mushrooms and Onions</span><span class="price">$8.00</span></li>
    <li class="menu-item"><span>Lamb Kibbeh &amp; Pinenuts (3 per serve)</span><span class="price">$7.50</span></li>
  </ul>

  <h2 class="section-heading" style="top:523px;">Traditional Hummus</h2>
  <p class="section-note" style="top:553px;">Served with 1 Laffa and Mixed Pickles</p>
  <ul class="menu-list hummus-list">
    <li class="menu-item"><span>Masabacha – served with Tahini and whole Chickpeas</span><span class="price">$11.90</span></li>
    <li class="menu-item"><span>Ful – served with warm, crushed Fava Beans</span><span class="price">$14.90</span></li>
    <li class="menu-item"><span>Mushroom – served with Pan Fried Mushrooms</span><span class="price">$14.90</span></li>
    <li class="menu-item"><span>Basar – served with Mince Lamb &amp; Pine nuts</span><span class="price">$16.50</span></li>
  </ul>

  <section class="platter">
    <h2 class="platter-heading">Salads &amp; Dips Platter</h2>
    <p class="platter-note">3 Choices &amp; Laffa for $15.00 or 6 choices &amp; 2 Laffa for $25.00</p>
    <ul class="platter-list left">
      <li>Hummus</li>
      <li>Tahini</li>
      <li>Baba Ganoush</li>
      <li>White Cabbage</li>
      <li>Chatzilim (Fried Eggplant)</li>
    </ul>
    <ul class="platter-list right">
      <li>Noa's Corn Salad</li>
      <li>Moroccan Carrot</li>
      <li>Roasted Beetroot</li>
      <li>Turkish Dip</li>
    </ul>
  </section>
</body>
</html>
```